New Company Business Card Design

I have a new company logo and I want a new business card design. I dont know if the logo file i attached is in the correct format or quality. We are a New York City Specialty construction Firm specializing in high risk out of the box projects. I want a simple and classy business card that people will his card is as crisp as the work his company does.

Target Market(s)

Clients in the heavy construction industry in New York City

Industry/Entity Type

Construction Company

Contact Information for Business Card

Simple Classy - DIFFERENT

Font styles to use
Other font styles liked:
• Mach the logo font in some way

Colors

Designer to choose colors to be used in the design.

Requirements
Must have
• Uniqueness
Nice to have
• Nothing particular - Just different and classy - Timeless
Should not have
• Goofy Shit or Gimmicky shit

```html
<!DOCTYPE html>
<html lang="en">
<head>
<meta charset="utf-8">
<title>Kestrel Builders – Business Cards</title>
<link href="https://fonts.googleapis.com/css2?family=Fira+Sans:wght@400;700;800&display=swap" rel="stylesheet">
<style>
  :root {
    --canvas: #e3e2de;
    --paper: #f7f7f5;
    --blue: #1f6cc1;
    --amber: #f4a823;
    --navy: #0e1a2c;
    --shadow: 0 6px 18px rgba(0, 0, 0, 0.18);
  }
  * { margin: 0; padding: 0; box-sizing: border-box; }
  html, body {
    width: 1200px; height: 600px; overflow: hidden;
    background: var(--canvas);
    font-family: "Fira Sans", Arial, sans-serif;
  }
  .sheet { position: relative; width: 1200px; height: 600px; }

  .theme-bright {
    --side: var(--blue);
    --stripe: var(--amber);
    --band: var(--blue);
    --band-text: var(--amber);
    --foot: var(--navy);
    --foot-text: #3d7fd0;
  }
  .theme-night {
    --side: var(--navy);
    --stripe: var(--blue);
    --band: var(--navy);
    --band-text: #2f72c8;
    --foot: var(--blue);
    --foot-text: var(--navy);
  }

  .card {
    position: absolute;
    width: 480px; height: 274px;
    background: var(--paper);
    box-shadow: var(--shadow);
    overflow: hidden;
  }
  .card-shapes { position: absolute; inset: 0; }

  .col-left  { left: 80px; }
  .col-right { left: 640px; }
  .row-top    { top: 17px; }
  .row-bottom { top: 309px; }

  /* Front */
  .wordmark {
    position: absolute;
    display: flex; align-items: center; gap: 8px;
    color: var(--blue);
    font-weight: 800;
    text-transform: uppercase;
    line-height: 1.05;
    letter-spacing: 0.5px;
  }
  .wordmark-square {
    width: 14px; height: 14px; background: var(--blue); flex: none;
  }
  .card-front .wordmark {
    left: 50%; top: 50%; transform: translate(-50%, -50%);
    font-size: 22px; text-align: center;
  }

  /* Back */
  .back-top { position: absolute; left: 0; top: 0; width: 100%; height: 70px; background: var(--paper); }
  .back-band { position: absolute; left: 0; top: 70px; width: 100%; height: 152px; background: var(--band); }
  .back-foot { position: absolute; left: 0; top: 222px; width: 100%; height: 52px; background: var(--foot); }
  .card-back .wordmark { left: 22px; top: 20px; font-size: 18px; }
  .pointer { position: absolute; left: 26px; top: 70px; }

  .holder-name {
    position: absolute; left: 24px; top: 104px;
    color: var(--band-text);
    font-weight: 700; font-size: 22px;
  }
  .contact-list {
    position: absolute; right: 22px; top: 82px;
    list-style: none; text-align: right;
    color: var(--band-text);
    font-size: 12px; line-height: 20px;
  }
  .contact-list li { display: flex; justify-content: flex-end; align-items: center; gap: 6px; }
  .contact-icon { width: 12px; height: 12px; flex: none; }
  .address {
    position: absolute; left: 22px; top: 240px;
    color: var(--foot-text);
    font-size: 12px;
  }
</style>
</head>
<body>
<main class="sheet">

  <!-- Bright edition -->
  <section class="card card-front theme-bright col-left row-top">
    <svg class="card-shapes" viewBox="0 0 480 274" aria-hidden="true">
      <polygon points="0,0 160,0 90,274 0,274" fill="var(--side)"/>
      <polygon points="160,0 172,0 102,274 90,274" fill="var(--stripe)"/>
      <polygon points="378,0 390,0 320,274 308,274" fill="var(--stripe)"/>
      <polygon points="390,0 480,0 480,274 320,274" fill="var(--side)"/>
    </svg>
    <div class="wordmark"><span class="wordmark-square"></span><span>Kestrel<br>Builders, Inc.</span></div>
  </section>

  <section class="card card-back theme-bright col-left row-bottom">
    <div class="back-top"></div>
    <div class="back-band"></div>
    <div class="back-foot"></div>
    <div class="wordmark"><span class="wordmark-square"></span><span>Kestrel Builders, Inc.</span></div>
    <svg class="pointer" width="16" height="14" viewBox="0 0 16 14" aria-hidden="true"><polygon points="0,0 16,0 8,14" fill="var(--band-text)"/></svg>
    <p class="holder-name">Marco T. Ferrante</p>
    <ul class="contact-list">
      <li>555-014-2271 | 555-018-3390
        <svg class="contact-icon" viewBox="0 0 12 12" aria-hidden="true"><rect width="12" height="12" rx="2" fill="currentColor"/><path d="M3.5 2.5 L5 2.5 L5.5 4.5 L4.6 5.2 Q5.5 7 6.8 7.4 L7.5 6.5 L9.5 7 L9.5 8.5 Q5 9.5 3.5 2.5Z" fill="var(--band)"/></svg></li>
      <li>MARCO@KESTRELBLD.COM
        <svg class="contact-icon" viewBox="0 0 12 12" aria-hidden="true"><rect width="12" height="12" rx="2" fill="currentColor"/><rect x="2.5" y="3.5" width="7" height="5" fill="none" stroke="var(--band)" stroke-width="1"/><path d="M2.5 3.5 L6 6.3 L9.5 3.5" fill="none" stroke="var(--band)" stroke-width="1"/></svg></li>
      <li>KESTRELBLD.COM
        <svg class="contact-icon" viewBox="0 0 12 12" aria-hidden="true"><rect width="12" height="12" rx="2" fill="currentColor"/><circle cx="6" cy="6" r="3.5" fill="none" stroke="var(--band)" stroke-width="1"/><path d="M2.5 6 H9.5 M6 2.5 V9.5" stroke="var(--band)" stroke-width="0.8"/></svg></li>
    </ul>
    <p class="address">214 Harbor Line Road | Linden | New Jersey 07036</p>
  </section>

  <!-- Night edition -->
  <section class="card card-front theme-night col-right row-top">
    <svg class="card-shapes" viewBox="0 0 480 274" aria-hidden="true">
      <polygon points="0,0 160,0 90,274 0,274" fill="var(--side)"/>
      <polygon points="160,0 172,0 102,274 90,274" fill="var(--stripe)"/>
      <polygon points="378,0 390,0 320,274 308,274" fill="var(--stripe)"/>
      <polygon points="390,0 480,0 480,274 320,274" fill="var(--side)"/>
    </svg>
    <div class="wordmark"><span class="wordmark-square"></span><span>Kestrel<br>Builders, Inc.</span></div>
  </section>

  <section class="card card-back theme-night col-right row-bottom">
    <div class="back-top"></div>
    <div class="back-band"></div>
    <div class="back-foot"></div>
    <div class="wordmark"><span class="wordmark-square"></span><span>Kestrel Builders, Inc.</span></div>
    <svg class="pointer" width="16" height="14" viewBox="0 0 16 14" aria-hidden="true"><polygon points="0,0 16,0 8,14" fill="var(--band-text)"/></svg>
    <p class="holder-name">Marco T. Ferrante</p>
    <ul class="contact-list">
      <li>555-014-2271 | 555-018-3390
        <svg class="contact-icon" viewBox="0 0 12 12" aria-hidden="true"><rect width="12" height="12" rx="2" fill="currentColor"/><path d="M3.5 2.5 L5 2.5 L5.5 4.5 L4.6 5.2 Q5.5 7 6.8 7.4 L7.5 6.5 L9.5 7 L9.5 8.5 Q5 9.5 3.5 2.5Z" fill="var(--band)"/></svg></li>
      <li>MARCO@KESTRELBLD.COM
        <svg class="contact-icon" viewBox="0 0 12 12" aria-hidden="true"><rect width="12" height="12" rx="2" fill="currentColor"/><rect x="2.5" y="3.5" width="7" height="5" fill="none" stroke="var(--band)" stroke-width="1"/><path d="M2.5 3.5 L6 6.3 L9.5 3.5" fill="none" stroke="var(--band)" stroke-width="1"/></svg></li>
      <li>KESTRELBLD.COM
        <svg class="contact-icon" viewBox="0 0 12 12" aria-hidden="true"><rect width="12" height="12" rx="2" fill="currentColor"/><circle cx="6" cy="6" r="3.5" fill="none" stroke="var(--band)" stroke-width="1"/><path d="M2.5 6 H9.5 M6 2.5 V9.5" stroke="var(--band)" stroke-width="0.8"/></svg></li>
    </ul>
    <p class="address">214 Harbor Line Road | Linden | New Jersey 07036</p>
  </section>

</main>
</body>
</html>
```